Tollo is the place for Used Car Inspections

Tollo ONLY sells Used Car Inspections.

We need a website that tells that story simply.

Please be original and don't just copy my mockup. I'm not a designer.

Reason: Too few designers(<10)...too many weak designs(>80). I have subsequently revised my brief, uploaded more defined mockup and have tried to inspire some originality. I have also invited add designs, some who have declined. Any suggestions. Any suggestions?

Reason: Still waiting on original designs

Target Market(s)

Car Buyers

Industry/Entity Type

Used Car

Logo Text

Tollo

Number of Pages Required

5+ page

Font styles to use
Sans Serif

Colors
33a6d7
ffc214

Requirements
Must have
• Why Tollo?
• -Top 5 Questions
• Tollo Certified
• -Graphic detailing inspection
• How it Works
• -Graphic-- 1. Find a Location 2. Personal/Vehicle Info Form 3. Purchase
• -Get a Tollo Inspection
• Get a Tollo Inspection
• -Find a Location
• -Personal/Vehicle info Form
• -Purchase
• Become a Tollo Dealer
• -Form
• -Upload Credentials
• About Us
• Contact Us
• Term & Conditions
• Privacy
• FAQ
• Press
• Social Media
Nice to have
• Customer feedback-Quorra
Should not have
• Not sure

```html
<!DOCTYPE html>
<html lang="en">
<head>
<meta charset="utf-8">
<title>Tollo – Used Car Inspections</title>
<link href="https://fonts.googleapis.com/css2?family=Open+Sans:wght@400;600;700;800&display=swap" rel="stylesheet">
<style>
:root{
  --blue:#33a6d7;
  --green:#8cc63f;
  --orange:#f7941d;
  --yellow:#ffc214;
  --ink:#2d2d2d;
  --muted:#7a7a7a;
  --hero:#ececec;
  --footer:#eeeeee;
  --bar:#2b2b2b;
  --white:#ffffff;
}
*{box-sizing:border-box;margin:0;padding:0}
html,body{width:719px;height:1200px;overflow:hidden}
body{font-family:"Open Sans",Arial,sans-serif;color:var(--ink);background:var(--white);position:relative}

/* header */
.site-header{height:78px;position:relative;border-bottom:1px solid #e4e4e4}
.brand{position:absolute;left:22px;top:16px;display:flex;align-items:center;gap:8px}
.brand-dot{width:34px;height:34px;border-radius:50%;background:var(--blue)}
.brand-name{font-size:30px;font-weight:800;color:var(--ink);letter-spacing:-.5px}
.utility{position:absolute;right:22px;top:14px;font-size:7.5px;color:var(--muted)}
.utility b{color:var(--blue);font-weight:600}
.main-nav{position:absolute;right:22px;top:44px;display:flex;gap:6px;font-size:9px;font-weight:600;color:#555}
.main-nav span.sep{color:#bbb}
.main-nav .active{color:var(--blue)}

/* hero */
.hero{height:290px;background:linear-gradient(180deg,#f4f4f4,var(--hero));position:relative}
.hero-photo{position:absolute;left:24px;top:18px;width:350px;height:240px;border-radius:3px;background:linear-gradient(160deg,#e3e3e3 0%,#d9b7b8 45%,#c98f91 70%,#d6d6d6 100%)}
.hero-copy{position:absolute;left:405px;top:80px}
.hero-title{font-size:23px;font-weight:600;color:var(--blue)}
.hero-title strong{color:var(--ink);font-weight:700}
.btn{display:inline-block;margin-top:14px;margin-left:62px;background:var(--orange);color:var(--white);font-size:11px;font-weight:600;padding:8px 14px;border-radius:2px}
.dots{position:absolute;left:50%;bottom:10px;transform:translateX(-50%);display:flex;gap:5px}
.dots i{width:7px;height:7px;border-radius:50%;background:#bdbdbd;display:block}
.dots i.on{background:#777}

/* audience band */
.audience{height:108px;position:relative;color:var(--white)}
.audience svg.band{position:absolute;inset:0}
.role{position:absolute;top:22px;display:flex;gap:14px;align-items:flex-start}
.role.seller{left:30px}
.role.buyer{left:400px}
.role-icon{width:50px;height:50px;border:2px solid var(--white);border-radius:50%;display:flex;align-items:center;justify-content:center}
.role h3{font-size:13px;font-weight:700;margin-top:4px}
.role p{font-size:7.5px;line-height:1.45;margin-top:4px;max-width:170px}

/* inspection */
.inspection{padding-top:50px}
.section-title{display:flex;align-items:center;justify-content:center;gap:14px;font-size:18px;font-weight:700;letter-spacing:.3px}
.section-title::before,.section-title::after{content:"";width:70px;height:1px;background:#ccc}
.section-title em{font-style:normal;color:var(--blue);font-weight:600}
.cards{display:flex;gap:16px;justify-content:center;margin-top:26px}
.card{width:142px;background:var(--white);box-shadow:0 1px 3px rgba(0,0,0,.18)}
.card-photo{height:106px}
.card-photo.p1{background:linear-gradient(135deg,#4a6f88,#c7b8a4)}
.card-photo.p2{background:linear-gradient(135deg,#8a1f22,#e8dcd2)}
.card-photo.p3{background:linear-gradient(135deg,#cfd8de,#6e7f8b)}
.card-photo.p4{background:linear-gradient(135deg,#5e6d78,#c9b59b)}
.card-body{padding:6px 7px 10px}
.card-body h4{font-size:8px;font-weight:600;color:var(--blue)}
.card-body p{font-size:6.5px;color:var(--muted);margin-top:2px}

/* testimonial */
.testimonial{margin:30px auto 0;width:604px;height:232px;border:8px solid #e2e2e2;position:relative}
.testimonial-photo{position:absolute;inset:0;background:linear-gradient(100deg,#8aa0ae 0%,#c7b7a2 40%,#e7d6c4 60%,#4b4f55 100%)}
.quote{position:absolute;right:16px;bottom:16px;color:var(--white);text-shadow:0 1px 2px rgba(0,0,0,.45)}
.quote .name{font-size:17px;font-weight:700}
.quote .who{font-size:10px;font-weight:600;margin-top:-2px}
.quote blockquote{font-size:11px;line-height:1.35;margin-top:6px;max-width:190px}
.testimonial .dots{left:22px;bottom:12px;transform:none}
.testimonial .dots i{background:rgba(255,255,255,.6)}
.testimonial .dots i.on{background:var(--white)}

/* footer */
.site-footer{position:absolute;left:0;right:0;top:1005px;height:160px;background:var(--footer);padding:20px 56px 0;display:flex;justify-content:space-between}
.foot-col h5{font-size:8px;font-weight:700;color:var(--blue);margin-bottom:7px}
.foot-col li{list-style:none;font-size:7px;color:#666;line-height:2}
.bottom-bar{position:absolute;left:0;right:0;bottom:0;height:35px;background:var(--bar);display:flex;align-items:center;justify-content:space-between;padding:0 20px}
.bottom-bar small{font-size:7px;color:#aaa}
.social{display:flex;gap:4px}
.social i{display:block;width:15px;height:15px}
</style>
</head>
<body>

<header class="site-header">
  <div class="brand"><span class="brand-dot"></span><span class="brand-name">Tollo</span></div>
  <div class="utility">Tech Questions · Tollo Certified · <b>Get an Inspection</b> · 800-555-0142</div>
  <nav class="main-nav">
    <span class="active">Home</span><span class="sep">|</span>
    <span>Why Tollo</span><span class="sep">|</span>
    <span>Get a Tollo Report</span><span class="sep">|</span>
    <span>Find a Tollo Location</span><span class="sep">|</span>
    <span>Be a Tollo Mechanic</span>
  </nav>
</header>

<section class="hero">
  <div class="hero-photo" role="img" aria-label="Photo of a red sedan on a light grey backdrop"></div>
  <div class="hero-copy">
    <h1 class="hero-title">Find A Tollo <strong>Used Car</strong></h1>
    <a class="btn">Get Tollo Inspection</a>
  </div>
  <div class="dots"><i class="on"></i><i></i><i></i><i></i><i></i></div>
</section>

<section class="audience">
  <svg class="band" width="719" height="108" viewBox="0 0 719 108">
    <rect width="719" height="108" fill="#8cc63f"/>
    <polygon points="0,0 340,0 382,54 340,108 0,108" fill="#33a6d7"/>
  </svg>
  <div class="role seller">
    <div class="role-icon">
      <svg width="24" height="24" viewBox="0 0 24 24" fill="#fff"><circle cx="12" cy="7" r="5"/><path d="M2 23c0-6 4.5-9 10-9s10 3 10 9z"/></svg>
    </div>
    <div>
      <h3>SELLER</h3>
      <p>Inspire buyer confidence<br>Sell your car for its true worth<br>Sell faster</p>
    </div>
  </div>
  <div class="role buyer">
    <div class="role-icon">
      <svg width="26" height="20" viewBox="0 0 26 20" fill="#fff"><path d="M4 8l3-6h12l3 6h2v7h-2v3h-4v-3H8v3H4v-3H2V8z"/><rect x="8" y="4" width="10" height="4" fill="#8cc63f"/><circle cx="7" cy="12" r="1.6" fill="#8cc63f"/><circle cx="19" cy="12" r="1.6" fill="#8cc63f"/></svg>
    </div>
    <div>
      <h3>BUYER</h3>
      <p>Buying a car from a private seller? Get the full picture before you pay, with a clear Tollo report.</p>
    </div>
  </div>
</section>

<section class="inspection">
  <h2 class="section-title"><span>TOLLO <em>INSPECTION</em></span></h2>
  <div class="cards">
    <article class="card"><div class="card-photo p1" role="img" aria-label="Driver seated in a car"></div><div class="card-body"><h4>139 Point Tollo</h4><p>Every part checked by a pro</p></div></article>
    <article class="card"><div class="card-photo p2" role="img" aria-label="Woman standing beside a red car"></div><div class="card-body"><h4>139 Point Tollo</h4><p>Clear report in plain words</p></div></article>
    <article class="card"><div class="card-photo p3" role="img" aria-label="Row of white cars on a lot"></div><div class="card-body"><h4>139 Point Tollo</h4><p>Know the car before you pay</p></div></article>
    <article class="card"><div class="card-photo p4" role="img" aria-label="Man standing next to a car"></div><div class="card-body"><h4>139 Point Tollo</h4><p>Buy with full confidence</p></div></article>
  </div>
</section>

<section class="testimonial">
  <div class="testimonial-photo" role="img" aria-label="Smiling customer leaning on her car holding keys in a city street"></div>
  <div class="quote">
    <div class="name">Marisa</div>
    <div class="who">Tollo Customer</div>
    <blockquote>"Not sure why anyone would buy a used car without a tollo inspection"</blockquote>
  </div>
  <div class="dots"><i class="on"></i><i></i><i></i><i></i><i></i></div>
</section>

<footer class="site-footer">
  <div class="foot-col"><h5>LINK</h5><ul><li>Sell a Car</li><li>Buy a Car</li><li>Weekend Driver</li><li>Tollo Love</li></ul></div>
  <div class="foot-col"><h5>SPECIALISTS</h5><ul><li>How it Works</li><li>Tollo Certified</li><li>Get Pricing Advantage</li><li>Seller Checklist</li></ul></div>
  <div class="foot-col"><h5>LINKS</h5><ul><li>FAQ</li><li>Coverage Area</li><li>Terms of Use</li><li>Privacy Policy</li></ul></div>
  <div class="foot-col"><h5>BUSINESS</h5><ul><li>Jobs</li><li>About Us</li><li>Contact Us</li><li>Press</li></ul></div>
  <div class="foot-col"><h5>CONTACT US</h5><ul><li>42 Linden Row, Brookvale 2100</li><li>Phone: 800-555-0142</li><li>E-mail: hello@tollo.example</li></ul></div>
</footer>

<div class="bottom-bar">
  <small>Copyright © 2015. All Rights Reserved.</small>
  <div class="social">
    <i style="background:var(--orange)"></i>
    <i style="background:var(--blue)"></i>
    <i style="background:#3b5998"></i>
    <i style="background:#d23f31"></i>
    <i style="background:#0e76a8"></i>
    <i style="background:#c4302b"></i>
  </div>
</div>

</body>
</html>
```